Financial Services Company Needs New UI/UX

Hello!

We would like to see some UI/UX ideas for our software platform. I've attached a screen capture of our current "dashboard" (or main home page, essentially). We're looking for a very simple, clean, sleek design as there are many different pages throughout the system that will all need to coordinate. You can also view our website to see the colors and general "look" we have on there. It would be ideal for the portal to coordinate with the website since that is how they access the login page. Please submit your best ideas for the dashboard and we will reach out to our favorite designer to move forward with the rest of the pages. You can find our color hex codes on our website on the "Media" page. Should you need any other supporting logos or files please send us a message and we will try to accommodate.

Thanks!

Website: www.ledgerharbor-example.com

Target Market(s)

Our clients are contractors in the construction industry and our software helps them manage material purchases for their jobs.

Industry/Entity Type

Financial Service

Font styles to use
Sans Serif

Requirements
Must have
• The same content and language as the current dashboard but an updated look.
Should not have
• Too much distraction or busy patterns, we're looking for clean and simple and user friendly. Likely a solid or subtly textured background would be best.

```html
<!DOCTYPE html>
<html lang="en">
<head>
<meta charset="utf-8">
<title>LedgerHarbor Dashboard</title>
<link href="https://fonts.googleapis.com/css2?family=Roboto:wght@300;400;500;700&display=swap" rel="stylesheet">
<style>
:root{
  --page:#e5e9ef;
  --card:#d8dde6;
  --card-alt:#d3d8e1;
  --inset:#e6e9ef;
  --accent:#4a88e5;
  --brand-blue:#4a8ae0;
  --amount:#e8612c;
  --ink:#333a44;
  --muted:#555b66;
  --divider:#c9ced8;
  --avatar:#4f5e7a;
  --white:#ffffff;
}
*{box-sizing:border-box;margin:0;padding:0}
html,body{width:1200px;height:900px;overflow:hidden}
body{background:var(--page);font-family:'Roboto',Arial,sans-serif;color:var(--ink);position:relative}
.abs{position:absolute}

/* header */
.brand{left:20px;top:38px;display:flex;align-items:center;gap:8px}
.brand-dot{width:34px;height:34px;border-radius:50%;background:var(--ink)}
.brand-name{font-size:17px;font-weight:400;color:var(--ink);letter-spacing:-.2px}
.divider{width:1px;background:var(--divider);top:16px;height:76px}
.page-title{left:230px;top:36px;font-size:31px;font-weight:300;color:var(--brand-blue)}
.avatar{left:428px;top:28px;width:54px;height:54px;border-radius:50%;background:var(--avatar)}
.greeting{left:498px;top:35px;font-size:13px;color:var(--ink);line-height:24px}
.menu-icon{left:1147px;top:40px}

/* summary cards */
.card{background:var(--card);top:134px;height:334px;text-align:center}
.card.alt{background:var(--card-alt)}
.card-title{position:absolute;left:0;right:0;top:42px;font-size:24px;font-weight:300;color:var(--ink)}
.amount{position:absolute;left:0;right:0;top:68px;color:var(--amount);font-weight:300;line-height:1}
.amount .cur{font-size:24px;vertical-align:top;position:relative;top:4px}
.amount .whole{font-size:50px}
.amount .cents{font-size:24px}
.inset{position:absolute;background:var(--inset);display:flex;flex-direction:column;justify-content:center;align-items:center}
.inset-label{font-size:13px;color:var(--ink)}
.inset-value{font-size:17px;color:var(--ink);margin-top:3px}
.detail-row{font-size:13px;line-height:21px}
.detail-row b{font-weight:400;font-size:17px}
.btn{position:absolute;top:248px;height:41px;background:var(--accent);color:var(--white);font-size:17px;font-weight:400;display:flex;align-items:center;justify-content:center}

/* lower panels */
.panel{background:var(--card);top:488px;height:392px}
.panel-title{position:absolute;left:26px;top:34px;font-size:24px;font-weight:300;color:var(--ink)}
.th{font-size:17px;font-weight:500;color:var(--ink)}
.row-band{background:var(--inset)}
.cell{font-size:15px;color:var(--muted);line-height:24px}
.job-cell{font-size:14px;color:var(--muted)}
.help{width:22px;height:22px;border-radius:50%;background:var(--accent);color:var(--white);font-size:14px;font-weight:700;display:flex;align-items:center;justify-content:center}
</style>
</head>
<body>

<header>
  <div class="abs brand"><span class="brand-dot"></span><span class="brand-name">LedgerHarbor</span></div>
  <div class="abs divider" style="left:206px"></div>
  <h1 class="abs page-title">Dashboard</h1>
  <div class="abs divider" style="left:404px"></div>
  <div class="abs avatar" role="img" aria-label="User profile picture"></div>
  <div class="abs greeting">Hello User,<br>6/30/2016&nbsp; 03:08:21 AM</div>
  <svg class="abs menu-icon" width="31" height="31" viewBox="0 0 31 31" aria-label="Menu">
    <rect x="0" y="0" width="14" height="14" fill="#3d85e0"/>
    <rect x="17" y="0" width="14" height="14" fill="#3d85e0"/>
    <rect x="0" y="17" width="14" height="14" fill="#3d85e0"/>
    <rect x="17" y="17" width="14" height="14" fill="#3d85e0"/>
  </svg>
</header>

<section class="abs card" style="left:20px;width:376px">
  <h2 class="card-title">Available Master Credit</h2>
  <div class="amount"><span class="cur">$</span><span class="whole">129,500</span><span class="cents">.00</span></div>
  <div class="inset" style="left:23px;top:176px;width:327px;height:54px">
    <span class="inset-label">Master Credit Limit</span>
    <span class="inset-value">$250,000.00</span>
  </div>
  <div class="btn" style="left:23px;width:327px">Setup New Job</div>
</section>

<section class="abs card" style="left:416px;width:368px">
  <h2 class="card-title">Last Payment</h2>
  <div class="amount"><span class="cur">$</span><span class="whole">500</span><span class="cents">.00</span></div>
  <div class="inset" style="left:19px;top:176px;width:327px;height:54px">
    <span class="inset-label">Last Payment Date</span>
    <span class="inset-value">6/28/2016</span>
  </div>
  <div class="btn" style="left:19px;width:155px">View Payments</div>
  <div class="btn" style="left:194px;width:152px">View Billings</div>
</section>

<section class="abs card alt" style="left:804px;width:376px">
  <h2 class="card-title">Next Payment</h2>
  <div class="amount"><span class="cur">$</span><span class="whole">158</span><span class="cents">.95</span></div>
  <div class="inset" style="left:23px;top:147px;width:327px;height:83px">
    <div class="detail-row">Due Date <b>7/11/2016</b></div>
    <div class="detail-row">Current Principal <b>$9,968.46</b></div>
    <div class="detail-row">Minimum Interest/Fee <b>$158.95</b></div>
  </div>
  <div class="btn" style="left:23px;width:327px">Make Payment</div>
</section>

<section class="abs panel" style="left:20px;width:570px">
  <h2 class="panel-title">Task Summary</h2>
  <span class="abs th" style="left:65px;top:88px">Task</span>
  <span class="abs th" style="left:241px;top:88px">Status</span>
  <span class="abs th" style="left:433px;top:88px">Received</span>

  <div class="abs row-band" style="left:22px;top:118px;width:523px;height:58px"></div>
  <div class="abs row-band" style="left:22px;top:238px;width:523px;height:58px"></div>

  <div class="abs help" style="left:31px;top:125px">?</div>
  <span class="abs cell" style="left:65px;top:124px">Supplier Invoice</span>
  <span class="abs cell" style="left:240px;top:124px">Confirmation by<br>Account Manager</span>
  <span class="abs cell" style="left:433px;top:124px">5/10/2016</span>

  <div class="abs help" style="left:31px;top:184px">?</div>
  <span class="abs cell" style="left:65px;top:184px">Supplier Invoice</span>
  <span class="abs cell" style="left:236px;top:184px">Confirmation by<br>Account Manager</span>
  <span class="abs cell" style="left:433px;top:184px">5/09/2016</span>

  <div class="abs help" style="left:31px;top:244px">?</div>
  <span class="abs cell" style="left:65px;top:243px">Supplier Invoice</span>
  <span class="abs cell" style="left:236px;top:243px">Confirmation by<br>Account Manager</span>
  <span class="abs cell" style="left:433px;top:243px">5/07/2016</span>

  <div class="abs help" style="left:31px;top:305px">?</div>
  <span class="abs cell" style="left:65px;top:304px">Supplier Invoice</span>
  <span class="abs cell" style="left:236px;top:304px">Confirmation by<br>Account Manager</span>
  <span class="abs cell" style="left:433px;top:304px">5/04/2016</span>
</section>

<section class="abs panel" style="left:610px;width:570px">
  <h2 class="panel-title" style="left:28px">Active Jobs</h2>
  <span class="abs th" style="left:31px;top:94px">Job #</span>
  <span class="abs th" style="left:116px;top:94px">Job Name</span>
  <span class="abs th" style="left:223px;top:94px">Status</span>
  <span class="abs th" style="left:303px;top:94px">Credit Limit</span>
  <span class="abs th" style="left:431px;top:94px">Avail, Credits</span>

  <div class="abs row-band" style="left:22px;top:130px;width:523px;height:32px"></div>
  <div class="abs row-band" style="left:22px;top:202px;width:523px;height:32px"></div>
  <div class="abs row-band" style="left:22px;top:275px;width:523px;height:32px"></div>

  <span class="abs job-cell" style="left:31px;top:138px">PC101-001</span>
  <span class="abs job-cell" style="left:114px;top:138px">Job #001</span>
  <span class="abs job-cell" style="left:221px;top:138px">Active</span>
  <span class="abs job-cell" style="left:303px;top:138px">$50,100,00</span>
  <span class="abs job-cell" style="left:430px;top:138px">$35,100,00</span>

  <span class="abs job-cell" style="left:31px;top:174px">PC101-002</span>
  <span class="abs job-cell" style="left:114px;top:174px">Job #002</span>
  <span class="abs job-cell" style="left:221px;top:174px">Active</span>
  <span class="abs job-cell" style="left:303px;top:174px">$40.000,00</span>
  <span class="abs job-cell" style="left:430px;top:174px">$2.000,00</span>

  <span class="abs job-cell" style="left:31px;top:210px">PC101-003</span>
  <span class="abs job-cell" style="left:114px;top:210px">Job #003</span>
  <span class="abs job-cell" style="left:221px;top:210px">Active</span>
  <span class="abs job-cell" style="left:303px;top:210px">$22,000,00</span>
  <span class="abs job-cell" style="left:430px;top:210px">$0,00</span>

  <span class="abs job-cell" style="left:31px;top:246px">PC101-004</span>
  <span class="abs job-cell" style="left:114px;top:246px">Job #004</span>
  <span class="abs job-cell" style="left:221px;top:246px">Active</span>
  <span class="abs job-cell" style="left:303px;top:246px">$10,400,00</span>
  <span class="abs job-cell" style="left:430px;top:246px">$10,400,00</span>
</section>

</body>
</html>
```